3 -4 PAGE GIFT CERTIFICATE REDEMPTION WEBSITE REVAMP

I am revamping the entire website at www.brightperksportal.net

Will have brand new theme and new logo. Name Of Company:
Bounty Motivation Delivery Networks
BMDN

OVERVIEW:
I NEED A 3-4 PAGE WEBSITE DESIGNED WITH CHECKOUT MODULE.
My company offers fully brandable and personalizable gift certificates good for travel, vacations, dining rewards, rebates, electronic gifts, etc. and I need to redesign the website where the fulfillment and redemption happens.

So the way it works is a business uses my online platform to create, brand and personalize these gift certificates. The business can brand the certificates in the upper right hand corner of each certificate where the “Compliments Of” area sits with their company logo, website, contact info, etc and can also personalize each individual gift certificate to a specific customer too. SEE EXAMPLE ATTACHED TO BRIEF.

The example I attached to this brief includes a logo which is really just a picture and under it there is 3 lines of text where the business can put a website, phone number and email.

On the left side of the top banner image you will see “Exclusively For”.

So now, after a customer enters their certificate ID #, the branding on the next page must match the Compliments Of area and also must personalize the Sales Page to the customer that is in the Exclusively For” area of the certificate…...

Page 1: LANDING PAGE
CONTENT:

Welcome to the online redemption source for vacation certificates, travel vouchers, digital electronic products, dining incentives, gas and grocery rewards and more!

ENTER YOUR CERTIFICATE ID #
ENTER YOUR EMAIL

Welcome to the online redemption system for vacation certificates, travel vouchers, rebates, digital products, dining incentives, gas and grocery rewards and more!

PLEASE ENTER A VALID CERTIFICATE ID NUMBER TO VIEW THE DETAILS AND TO REDEEM AND ACTIVATE YOUR SPECIAL OFFER.

Also we need a testimonial module ON THIS PAGE AND SALES PAGE

PAGE 2: SALES PAGE FOR OFFER (we will use the 1-4 Night Las Vegas Hotel Stay Certificate)
INSTRUCTIONS EXPLANATION FOR DESIGNER: Every gift certificate has a "Compliments Of Area" in the upper right hand corner....SEE SAMPLE ATTACHED TO BRIEF. On the sales page we also show this to the customer after they enter the code. Every certificate has a Compliments Of area and we will also add "Exclusively For" so the person that is giving the certificate away can specify the name of the recipient so we will also transffer this information over to the SALES PAGE.

CONTENT FOR SALES PAGE:

WELCOME ~~NAME OF PERSON IN EXCLUSIVELY FOR AREA ON CERTIFICATE~~ !!

THIS SPECIAL INCENTIVE OFFER IS COMPLIMENTS OF

~~LOGO THAT IS SEEN ON CERTIFICATE~~
~~TEXT LINE 1~~
~~TEXT LINE 2~~
~~TEXT LINE 3~~

TITLE OF OFFER: STAY & PLAY IN LAS VEGAS FOR UP TO 4 NIGHTS!
There is no doubt that Las Vegas is one of the hottest travel destinations around the world. In fact, some people would even go as far as saying that perhaps it is THE hottest place to visit. Enjoy up to 4 nights of resort/casino accommodations in exciting Las Vegas, NV. Millions of people travel to this exciting city each year to enjoy its thrills. Thanks to the business you received this certificate from, now you can enjoy Las Vegas, NV too!

Features:
*Travel 7 Days A Week
*Stay Your Choice Of Nights (1-4 Nights)
*Good For Two Adults & Two Children
*Pay Just The Taxes & Fees
*Multiple Travel Date Requests Allowed
*Fully Transferable To Another Person
*Just A 30 Days Advance Notice Required
*You Will Have 12 Months To Complete Travel

HOW CAN WE DO THIS?

We contract with the world leading hotel chains and resorts to help them fill their otherwise empty rooms.

We help fill empty rooms which the hotels, resorts and cruise lines turn into additional revenue from other areas of their property and future bookings.

Hotels rarely experience full occupancy, yet they remain open, providing rooms and services at fixed costs. So when hotels give out their rooms by partnering with marketing companies like us, they might miss out on the room fee, but they already didn't have that in the first place, at least now they have the opportunity to gain a customer for their in-house restaurants, room service, their casinos, an extra day stay, future bookings, etc.

The magic of why our program works so well is the fact that it’s a win win for everyone involved. You win because you received a huge savings. The business who gave you the certificate wins because now you will remember them the next time you need the same kind of product or service that they provide and you might even refer your friends and family members. The hotels and resorts win because they gain additional revenue from other areas of their establishment that they otherwise would not have been able to get and they also have a new client that may book with them in the future. Remember, they didn’t have anyone in the room in the first place so since you are paying the normal rack rate you might be more inclined to spend your money at the hotel. You are never under any obligation to do so though!

Retail Value: Up to $826.00 (based on $159.00 per night)

How it Works:
You will receive up to 4 nights in a 3 star or better Las Vegas resort and casino for up to 4 travelers, 2 adults and 2 children.

Simply redeem the certificate to activate the travel period for 1 year. This means you will have at least 1 year to travel from the date you redeem and activate your offer. Be sure to redeem your certificate before it expires! All certificates will have an accompanying expiration date attached to them.

When you are ready to book you will simply have to pay the daily room rate taxes and fees of approximately $12-$33 per night (not per person). On average the taxes and fees come out to about $19 per night. (Retail Value: Up to $826.00 based on $159.00 per night)

Step 1: Redeem your certificate to activate your offer

Step 2: Fill out the online reservation request form with travel dates within the next 12 months.

Step 3: Wait for a confirmation of your booked reservation. You will be notified immediately upon us booking your reservation.

Go on your vacation and thank the business who gave you this special offer by doing business with them again and referring your friends and family members!

No timeshares or sales presentations, Guaranteed!

PAGE 3 IS CHECKOUT PAGE:

PLEASE USE ****HERE IS SAMPLE CODE FOR YOU TO TEST OUT AT CURRENT REDEMPTION PROCESS WWW.BRIGHTPERKSPORTAL.NET 46205-17938

TO SEE THE CURRENT CHECK OUT. I NEED ALL THE SAME CONTENT JUST A DIFFERENT MORE EFFICIENT CHECKOUT PROCESS HERE. OMIT THE LEFT SIDE OF THE CURRENT CHECK OUT PROCESS AS THIS CURRENT PROCESSS IS ONE STEP AND DOES NOT HAVE A SALES PAGE BUT NOW I AM CREATING A SALES PAGE BEFORE THE CHECKOUT SO THE BRANDING AND PERSONALIZATION WILL HAPPEN ON THE SALES PAGE….THANK YOU

Target Market(s)

END USERS THAT ARE REDEEMING SPECIAL OFFERS GIFT CERTIFICATES

Industry/Entity Type

Marketing

Number of Pages Required

4 page

Colors

Designer to choose colors to be used in the design.

Requirements
Must have
• OVERVIEW:
• I NEED A 3-4 PAGE WEBSITE DESIGNED WITH CHECKOUT MODULE.
• My company offers fully brandable and personalizable gift certificates good for travel, vacations, dining rewards, rebates, electronic gifts, etc. and I need to redesign the website where the fulfillment and redemption happens.
• So the way it works is a business uses my online platform to create, brand and personalize these gift certificates. The business can brand the certificates in the upper right hand corner of each certificate where the “Compliments Of” area sits with their company logo, website, contact info, etc and can also personalize each individual gift certificate to a specific customer too. SEE EXAMPLE ATTACHED TO BRIEF.
• The example I attached to this brief includes a logo which is really just a picture and under it there is 3 lines of text where the business can put a website, phone number and email.
• On the left side of the top banner image you will see “Exclusively For”.
• So now, after a customer enters their certificate ID #, the branding on the next page must match the Compliments Of area and also must personalize the Sales Page to the customer that is in the Exclusively For” area of the certificate…...
• Page 1: LANDING PAGE
• CONTENT:
• Welcome to the online redemption source for vacation certificates, travel vouchers, digital electronic products, dining incentives, gas and grocery rewards and more!
• ENTER YOUR CERTIFICATE ID #
• ENTER YOUR EMAIL
• Welcome to the online redemption system for vacation certificates, travel vouchers, rebates, digital products, dining incentives, gas and grocery rewards and more!
• PLEASE ENTER A VALID CERTIFICATE ID NUMBER TO VIEW THE DETAILS AND TO REDEEM AND ACTIVATE YOUR SPECIAL OFFER.
• Also we need a testimonial module ON THIS PAGE AND SALES PAGE
• PAGE 2: SALES PAGE FOR OFFER (we will use the 1-4 Night Las Vegas Hotel Stay Certificate)
• INSTRUCTIONS EXPLANATION FOR DESIGNER: Every gift certificate has a "Compliments Of Area" in the upper right hand corner....SEE SAMPLE ATTACHED TO BRIEF. On the sales page we also show this to the customer after they enter the code. Every certificate has a Compliments Of area and we will also add "Exclusively For" so the person that is giving the certificate away can specify the name of the recipient so we will also transffer this information over to the SALES PAGE.
• CONTENT FOR SALES PAGE:
• WELCOME ~~NAME OF PERSON IN EXCLUSIVELY FOR AREA ON CERTIFICATE~~ !!
• THIS SPECIAL INCENTIVE OFFER IS COMPLIMENTS OF
• ~~LOGO THAT IS SEEN ON CERTIFICATE~~
• ~~TEXT LINE 1~~
• ~~TEXT LINE 2~~
• ~~TEXT LINE 3~~
• TITLE OF OFFER: STAY & PLAY IN LAS VEGAS FOR UP TO 4 NIGHTS!
• There is no doubt that Las Vegas is one of the hottest travel destinations around the world. In fact, some people would even go as far as saying that perhaps it is THE hottest place to visit. Enjoy up to 4 nights of resort/casino accommodations in exciting Las Vegas, NV. Millions of people travel to this exciting city each year to enjoy its thrills. Thanks to the business you received this certificate from, now you can enjoy Las Vegas, NV too!
• Features:
• *Travel 7 Days A Week
• *Stay Your Choice Of Nights (1-4 Nights)
• *Good For Two Adults & Two Children
• *Pay Just The Taxes & Fees
• *Multiple Travel Date Requests Allowed
• *Fully Transferable To Another Person
• *Just A 30 Days Advance Notice Required
• *You Will Have 12 Months To Complete Travel
• HOW CAN WE DO THIS?
• We contract with the world leading hotel chains and resorts to help them fill their otherwise empty rooms.
• We help fill empty rooms which the hotels, resorts and cruise lines turn into additional revenue from other areas of their property and future bookings.
• Hotels rarely experience full occupancy, yet they remain open, providing rooms and services at fixed costs. So when hotels give out their rooms by partnering with marketing companies like us, they might miss out on the room fee, but they already didn't have that in the first place, at least now they have the opportunity to gain a customer for their in-house restaurants, room service, their casinos, an extra day stay, future bookings, etc.
• The magic of why our program works so well is the fact that it’s a win win for everyone involved. You win because you received a huge savings. The business who gave you the certificate wins because now you will remember them the next time you need the same kind of product or service that they provide and you might even refer your friends and family members. The hotels and resorts win because they gain additional revenue from other areas of their establishment that they otherwise would not have been able to get and they also have a new client that may book with them in the future. Remember, they didn’t have anyone in the room in the first place so since you are paying the normal rack rate you might be more inclined to spend your money at the hotel. You are never under any obligation to do so though!
• Retail Value: Up to $826.00 (based on $159.00 per night)
• How it Works:
• You will receive up to 4 nights in a 3 star or better Las Vegas resort and casino for up to 4 travelers, 2 adults and 2 children.
• Simply redeem the certificate to activate the travel period for 1 year. This means you will have at least 1 year to travel from the date you redeem and activate your offer. Be sure to redeem your certificate before it expires! All certificates will have an accompanying expiration date attached to them.
• When you are ready to book you will simply have to pay the daily room rate taxes and fees of approximately $12-$33 per night (not per person). On average the taxes and fees come out to about $19 per night. (Retail Value: Up to $826.00 based on $159.00 per night)
• Step 1: Redeem your certificate to activate your offer
• Step 2: Fill out the online reservation request form with travel dates within the next 12 months.
• Step 3: Wait for a confirmation of your booked reservation. You will be notified immediately upon us booking your reservation.
• Go on your vacation and thank the business who gave you this special offer by doing business with them again and referring your friends and family members!
• No timeshares or sales presentations, Guaranteed!
• PAGE 3 IS CHECKOUT PAGE:
• PLEASE USE ****HERE IS SAMPLE CODE FOR YOU TO TEST OUT AT CURRENT REDEMPTION PROCESS WWW.BRIGHTPERKSPORTAL.NET 46205-17938
• TO SEE THE CURRENT CHECK OUT. I NEED ALL THE SAME CONTENT JUST A DIFFERENT MORE EFFICIENT CHECKOUT PROCESS HERE. OMIT THE LEFT SIDE OF THE CURRENT CHECK OUT PROCESS AS THIS CURRENT PROCESSS IS ONE STEP AND DOES NOT HAVE A SALES PAGE BUT NOW I AM CREATING A SALES PAGE BEFORE THE CHECKOUT SO THE BRANDING AND PERSONALIZATION WILL HAPPEN ON THE SALES PAGE….THANK YOU
Nice to have
• OVERVIEW:
• Page 1: LANDING PAGE
• CONTENT:
• ENTER YOUR EMAIL
• CONTENT FOR SALES PAGE:
• ~~TEXT LINE 1~~
• ~~TEXT LINE 2~~
• ~~TEXT LINE 3~~
• Features:
• *Travel 7 Days A Week
• HOW CAN WE DO THIS?
• How it Works:
Should not have
• OVERVIEW:
• Page 1: LANDING PAGE
• CONTENT:
• ENTER YOUR EMAIL
• CONTENT FOR SALES PAGE:
• ~~TEXT LINE 1~~
• ~~TEXT LINE 2~~
• ~~TEXT LINE 3~~
• Features:
• *Travel 7 Days A Week
• HOW CAN WE DO THIS?
• How it Works:

```html
<!DOCTYPE html>
<html lang="en">
<head>
<meta charset="utf-8">
<title>BrightPerksPortal – Redemption Processing Center</title>
<link href="https://fonts.googleapis.com/css2?family=Poppins:wght@300;400;500;600;700&display=swap" rel="stylesheet">
<style>
:root{
  --gold:#cf9b33;
  --orange:#e8742a;
  --teal:#4db3c4;
  --ink:#1f2329;
  --text:#3b3f46;
  --muted:#8a9099;
  --gray:#e6e8ec;
  --footer:#434a54;
  --footer-text:#c5c9cf;
  --white:#ffffff;
}
*{margin:0;padding:0;box-sizing:border-box}
html,body{width:759px;height:1200px;overflow:hidden;background:var(--white)}
body{font-family:'Poppins',sans-serif;color:var(--text)}
.page{position:relative;width:759px;height:1200px;overflow:hidden;background:var(--white)}

/* header */
.site-header{position:absolute;left:0;top:0;width:759px;height:76px;background:var(--white)}
.brand{position:absolute;left:81px;top:22px;display:flex;flex-direction:column}
.brand-row{display:flex;align-items:center;gap:5px}
.brand-dot{width:9px;height:9px;border-radius:50%;background:var(--gold)}
.brand-name{font-weight:700;font-size:16px;color:var(--orange);letter-spacing:-.2px;line-height:18px}
.brand-tag{font-size:6px;color:var(--ink);margin-left:22px;margin-top:3px}
.main-nav{position:absolute;left:299px;top:31px;display:flex;font-size:7.6px}
.main-nav a{color:var(--text);text-decoration:none;position:absolute;white-space:nowrap}
.main-nav a.active{color:var(--teal)}
.btn{display:flex;align-items:center;justify-content:center;background:var(--gold);color:var(--white);font-weight:600;border-radius:12px;text-decoration:none}
.header-cta{position:absolute;left:552px;top:27px;width:126px;height:23px;font-size:7.4px}

/* hero */
.hero{position:absolute;left:0;top:76px;width:759px;height:354px}
.hero-photo{position:absolute;inset:0;background:
  radial-gradient(ellipse 260px 140px at 640px 80px,rgba(200,215,225,.55),transparent),
  radial-gradient(ellipse 200px 180px at 620px 280px,rgba(60,120,110,.6),transparent),
  linear-gradient(180deg,#5d6770 0%,#7b8288 45%,#6a6458 75%,#4c4a44 100%)}
.hero-copy{position:absolute;left:81px;top:74px;width:290px;color:var(--white)}
.hero-copy h1{font-size:18.5px;font-weight:600;line-height:21px;letter-spacing:.2px}
.hero-copy p{font-size:7.5px;line-height:12px;margin-top:9px}
.field{position:absolute;left:81px;width:182px;height:25px;border:1px solid var(--white);border-radius:13px;color:var(--white);font-size:7.4px;padding-left:15px;display:flex;align-items:center}
.field-id{top:165px}
.field-email{top:200px}
.submit-arrow{position:absolute;left:87px;top:246px;width:25px;height:25px}
.hero-curve{position:absolute;left:0;top:0}

/* intro */
.intro{position:absolute;left:0;top:426px;width:759px;text-align:center}
.intro h2{font-size:13px;font-weight:600;color:var(--ink)}
.intro p{font-size:10.6px;font-weight:300;line-height:15px;color:var(--ink);width:390px;margin:6px auto 0}
.intro-cta{position:absolute;left:329px;top:70px;width:101px;height:23px;font-size:7.4px;border-radius:12px}
.gift-cards{position:absolute;left:0;top:540px;width:759px;height:92px}

/* testimonials */
.testimonials{position:absolute;left:0;top:632px;width:759px;height:320px;background:var(--gray)}
.testimonials h2{position:absolute;width:100%;top:48px;text-align:center;font-size:13px;font-weight:600;color:var(--text)}
.quote-card{position:absolute;top:86px;width:286px;height:152px;background:var(--white);box-shadow:0 6px 14px rgba(0,0,0,.05);padding:22px 25px 0}
.quote-card::before,.quote-card::after{content:"";position:absolute;left:0;width:100%;height:4px;background:radial-gradient(circle at 4px 0,var(--gray) 2.6px,transparent 3px) repeat-x;background-size:8px 4px}
.quote-card::before{top:0}
.quote-card::after{bottom:0;transform:rotate(180deg)}
.card-left{left:81px}
.card-right{left:392px}
.quote-head{display:flex;align-items:center;font-size:10px}
.quote-mark{width:20px;height:13px;margin-right:8px}
.quote-name{font-weight:600;color:var(--text)}
.quote-sep{color:var(--muted);margin:0 6px;font-weight:300}
.quote-place{color:#a7adb5;font-weight:300}
.quote-body{font-size:7.3px;line-height:12.2px;margin-top:10px;color:var(--text)}
.quote-date{position:absolute;left:25px;top:123px;font-size:5.8px;color:var(--teal)}
.slider-arrow{position:absolute;top:156px;width:8px;height:14px}
.dots{position:absolute;top:266px;left:358px;display:flex;gap:3px}
.dots span{width:6px;height:6px;border-radius:50%;border:.8px solid var(--muted)}
.dots span.on{background:radial-gradient(circle,var(--muted) 1.3px,transparent 1.6px)}

/* footer */
.site-footer{position:absolute;left:0;top:920px;width:759px;height:280px}
.footer-bg{position:absolute;left:0;top:0}
.footer-col{position:absolute;top:100px;color:var(--footer-text)}
.footer-col h3{font-size:10px;font-weight:500;color:var(--white);margin-bottom:13px}
.col-contact{left:81px}
.col-links{left:406px}
.col-social{left:521px}
.contact-line{display:flex;align-items:center;gap:8px;font-size:7.4px}
.contact-line svg{width:10px;height:10px}
.contact-phone{font-size:10px;font-weight:300}
.contact-address{display:flex;gap:8px;margin-top:14px;font-size:7.4px;line-height:12px}
.contact-address strong{font-weight:600}
.link-list{list-style:none;font-size:7.4px;line-height:15.2px}
.social-row{display:flex;gap:5px;margin-top:-1px}
.social-row span{width:25px;height:25px;border:1px solid var(--footer-text);border-radius:50%}
.footer-rule{position:absolute;left:56px;top:239px;width:647px;height:1px;background:#5b626c}
.copyright{position:absolute;top:254px;width:100%;text-align:center;font-size:7px;color:var(--footer-text)}
</style>
</head>
<body>
<div class="page">

  <header class="site-header">
    <div class="brand">
      <div class="brand-row"><span class="brand-dot"></span><span class="brand-name">BrightPerksPortal</span></div>
      <span class="brand-tag">Redemption Processing Center</span>
    </div>
    <nav class="main-nav">
      <a class="active" style="left:0">Home</a>
      <a style="left:45px">Sale</a>
      <a style="left:83px">Testimonials</a>
      <a style="left:154px">About</a>
      <a style="left:199px">Contact</a>
    </nav>
    <a class="btn header-cta">Design A Gift Certificate</a>
  </header>

  <section class="hero">
    <div class="hero-photo" role="img" aria-label="Collage of world landmarks with a passenger jet flying overhead"></div>
    <div class="hero-copy">
      <h1>Welcome to the online redemption source</h1>
      <p>Please enter a valid certificate id number to view the details and to redeem and activate your special offer.</p>
    </div>
    <div class="field field-id">Enter your Certificate Id #</div>
    <div class="field field-email">Email Address</div>
    <svg class="submit-arrow" viewBox="0 0 25 25" aria-label="Submit">
      <circle cx="12.5" cy="12.5" r="12.5" fill="#cf9b33"/>
      <path d="M7 12.5h10M13 8.5l4 4-4 4" stroke="#fff" stroke-width="1.3" fill="none" stroke-linecap="round" stroke-linejoin="round"/>
    </svg>
    <svg class="hero-curve" width="759" height="354" viewBox="0 0 759 354">
      <path d="M0 354 Q380 222 759 354 Z" fill="#fff"/>
      <path d="M94 335 Q380 265 665 335" stroke="#cf9b33" stroke-width="2.6" fill="none"/>
    </svg>
  </section>

  <section class="intro">
    <h2>Online redemption system for</h2>
    <p>vacation certificates, travel vouchers, rebates, digital products, dining incentives, gas and grocery rewards and more!</p>
    <a class="btn intro-cta">Get Started Now!</a>
  </section>

  <svg class="gift-cards" viewBox="0 0 759 92" role="img" aria-label="Fan of assorted branded gift cards">
    <g transform="translate(0,0)">
      <rect x="222" y="20" width="60" height="95" rx="3" fill="#0d1458" transform="rotate(-15 252 67)"/>
      <rect x="255" y="20" width="60" height="95" rx="3" fill="#0c5a3b" transform="rotate(-25 285 67)"/>
      <rect x="300" y="18" width="58" height="95" rx="3" fill="#ececec" transform="rotate(-20 329 65)"/>
      <rect x="350" y="25" width="62" height="95" rx="3" fill="#b2307f" transform="rotate(30 381 72)"/>
      <rect x="400" y="20" width="58" height="95" rx="3" fill="#26a98f" transform="rotate(15 429 67)"/>
      <rect x="440" y="20" width="58" height="95" rx="3" fill="#1a5ea6" transform="rotate(25 469 67)"/>
      <rect x="478" y="16" width="56" height="95" rx="3" fill="#f6b447" transform="rotate(15 506 63)"/>
    </g>
  </svg>

  <section class="testimonials">
    <h2>Testimonials</h2>
    <svg class="slider-arrow" style="left:36px" viewBox="0 0 8 14"><path d="M7 1 1 7l6 6" stroke="#8a9099" fill="none"/></svg>
    <svg class="slider-arrow" style="left:716px" viewBox="0 0 8 14"><path d="M1 1l6 6-6 6" stroke="#8a9099" fill="none"/></svg>

    <article class="quote-card card-left">
      <div class="quote-head">
        <svg class="quote-mark" viewBox="0 0 20 13"><path d="M8 1H2v11h6V6H3.5M18 1h-6v11h6V6h-4.5" stroke="#cf9b33" stroke-width="1.3" fill="none"/></svg>
        <span class="quote-name">Marcus T.</span><span class="quote-sep">|</span><span class="quote-place">Duluth, GA</span>
      </div>
      <p class="quote-body">I worked with the travel agency and they were very patient with me as I narrowed down where myself and another friend wanted to travel to. I gave them destinations and in return they gave me prompt responses ...</p>
      <span class="quote-date">- 21 Jan 2020 09:27:24 pm</span>
    </article>

    <article class="quote-card card-right">
      <div class="quote-head">
        <svg class="quote-mark" viewBox="0 0 20 13"><path d="M8 1H2v11h6V6H3.5M18 1h-6v11h6V6h-4.5" stroke="#cf9b33" stroke-width="1.3" fill="none"/></svg>
        <span class="quote-name">Elena P.</span><span class="quote-sep">|</span><span class="quote-place">Flagstaff, AZ</span>
      </div>
      <p class="quote-body">Wonderful! It was just like being in Rome, but only with great shows to enjoy. The rooms of the Solara and service were excellent. Going through the travel agency was simple and easy on the purse strings.</p>
      <span class="quote-date">- 21 Jan 2020 09:03:06 pm</span>
    </article>

    <div class="dots"><span class="on"></span><span></span><span></span><span></span><span></span></div>
  </section>

  <footer class="site-footer">
    <svg class="footer-bg" width="759" height="280" viewBox="0 0 759 280">
      <path d="M0 77 Q380 -55 759 77 V280 H0 Z" fill="#434a54"/>
      <path d="M94 58 Q380 -10 665 58" stroke="#cf9b33" stroke-width="2.6" fill="none"/>
    </svg>

    <div class="footer-col col-contact">
      <h3>Have A Question? Contact Us Today!</h3>
      <div class="contact-line contact-phone">
        <svg viewBox="0 0 10 10"><path d="M2 1l2 2-1 1.2c.6 1.2 1.6 2.2 2.8 2.8L7 6l2 2-1.3 1.3C4.5 9 1 5.5.7 2.3Z" stroke="#c5c9cf" stroke-width=".7" fill="none"/></svg>
        <span>Call. 1-800-555-0148</span>
      </div>
      <div class="contact-line" style="margin-top:5px">
        <svg viewBox="0 0 10 10"><rect x="1" y="2.5" width="8" height="5.5" stroke="#c5c9cf" stroke-width=".7" fill="none"/><path d="M1 2.5l4 3 4-3" stroke="#c5c9cf" stroke-width=".7" fill="none"/></svg>
        <span>e. hello@brightperksportal.net</span>
      </div>
      <div class="contact-address">
        <svg width="10" height="10" viewBox="0 0 10 10"><path d="M5 9.5S1.8 6 1.8 4a3.2 3.2 0 0 1 6.4 0C8.2 6 5 9.5 5 9.5Z" stroke="#c5c9cf" stroke-width=".7" fill="none"/><circle cx="5" cy="4" r="1" stroke="#c5c9cf" stroke-width=".7" fill="none"/></svg>
        <div><strong>The Rewards Desk</strong><br>2450 Harbor View Rd Ste B #112<br>Oakdale, Ca 92107</div>
      </div>
    </div>

    <div class="footer-col col-links">
      <h3>Quick Link</h3>
      <ul class="link-list"><li>Sale</li><li>Testimonials</li><li>About</li><li>Contact</li><li>Terms</li></ul>
    </div>

    <div class="footer-col col-social">
      <h3>Get Social</h3>
      <div class="social-row">
        <span role="img" aria-label="Social profile link"></span>
        <span role="img" aria-label="Social profile link"></span>
        <span role="img" aria-label="Video channel link"></span>
        <span role="img" aria-label="Professional network link"></span>
      </div>
    </div>

    <div class="footer-rule"></div>
    <p class="copyright">©2019 The Rewards Desk. All rights reserved.</p>
  </footer>

</div>
</body>
</html>
```